Web Design Project - Homepage mockup for media services company

Client would like a site much like this example below in terms of design and layout:

http://fernquill.net/

It's a media services company and the services they provide are:
-audio/video production
-graphic design
-social media
-web development
-apparel design

Their logo file is attached. I have also attached some of their service descriptions if that at all helps with things.

```html
<!DOCTYPE html>
<html lang="en">
<head>
<meta charset="utf-8">
<title>L. Marvelo — Media Services</title>
<link href="https://fonts.googleapis.com/css2?family=Ubuntu:wght@400;500;700&family=Arimo:wght@400;700&display=swap" rel="stylesheet">
<style>
  :root {
    --topbar: #2b2b2b;
    --header-top: #ffffff;
    --header-bottom: #e4e4e4;
    --maroon-dark: #2a0708;
    --maroon: #4a1114;
    --accent: #7a1c1c;
    --ink: #222222;
    --body-text: #4a4a4a;
    --panel: #f3f6f7;
    --panel-edge: #e9eef0;
    --footer: #2e2e2e;
    --footer-text: #e2e2e2;
    --white: #ffffff;
  }
  * { box-sizing: border-box; margin: 0; padding: 0; }
  html, body { width: 1200px; height: 1160px; overflow: hidden; }
  body { position: relative; background: var(--panel-edge); font-family: "Arimo", Arial, sans-serif; color: var(--ink); }

  .topbar { position: absolute; left: 0; top: 0; width: 1200px; height: 32px; background: var(--topbar); }
  .topbar__links { position: absolute; right: 118px; top: 8px; font-size: 11px; color: #9a9a9a; letter-spacing: -0.2px; display: flex; align-items: center; gap: 4px; }
  .topbar__links b { font-weight: 400; color: #c9c9c9; }
  .topbar__links svg { margin-left: 6px; }

  .site-header { position: absolute; left: 0; top: 32px; width: 1200px; height: 131px; background: linear-gradient(var(--header-top), var(--header-bottom)); }
  .brand { position: absolute; left: 130px; top: 26px; display: flex; align-items: center; gap: 12px; }
  .brand__mark { width: 56px; height: 56px; border-radius: 50%; background: #2a2a2a; }
  .brand__name { font-family: "Ubuntu", sans-serif; font-size: 34px; font-weight: 400; color: #2a2a2a; }

  .main-nav { position: absolute; left: 538px; top: 68px; display: flex; font-family: "Ubuntu", sans-serif; font-size: 20px; }
  .main-nav a { color: var(--ink); text-decoration: none; padding: 0 22px; border-left: 1px solid #cfcfcf; line-height: 28px; }
  .main-nav a:first-child { padding-left: 0; border-left: none; }
  .main-nav a:last-child { padding-right: 0; }
  .main-nav a.is-active { color: var(--accent); }

  .hero { position: absolute; left: 0; top: 163px; width: 1200px; height: 468px; background: radial-gradient(ellipse at 50% 40%, var(--maroon) 0%, var(--maroon-dark) 100%); overflow: hidden; }
  .hero__bubble { position: absolute; border-radius: 50%; background: rgba(255,255,255,0.05); }
  .hero__photo { position: absolute; left: 144px; top: 57px; width: 906px; height: 353px; border: 1px solid #7a2a2a; background: linear-gradient(100deg, #2b2f35 0%, #5c6470 45%, #8a3b3f 75%, #b6babd 100%); }
  .hero__caption { position: absolute; left: 144px; top: 105px; width: 396px; height: 178px; background: rgba(20,20,20,0.78); padding: 8px 14px 0 14px; }
  .hero__title { font-family: "Ubuntu", sans-serif; font-weight: 500; font-size: 29px; line-height: 36px; color: var(--white); letter-spacing: 0.3px; }
  .hero__text { margin-top: 8px; padding-left: 3px; width: 368px; font-size: 13.5px; line-height: 18px; color: var(--white); }
  .hero__button { display: inline-block; margin: 12px 0 0 3px; padding: 0 11px; height: 24px; line-height: 24px; border-radius: 3px; background: linear-gradient(#6b1a1e, #3f0c0f); border: 1px solid #8a2a2e; font-family: "Ubuntu", sans-serif; font-size: 12px; color: var(--white); }
  .hero__arrow { position: absolute; top: 206px; width: 44px; height: 44px; }

  .services { position: absolute; left: 10px; top: 631px; width: 1180px; height: 422px; background: var(--panel); }
  .service { position: absolute; top: 26px; width: 300px; }
  .service__title { font-family: "Ubuntu", sans-serif; font-weight: 400; font-size: 24px; line-height: 28px; color: #3a3a3a; text-align: center; }
  .service__art { margin: 14px auto 0; width: 116px; height: 116px; border-radius: 6px; }
  .service__text { margin-top: 12px; padding: 0 4px; font-size: 12px; line-height: 18px; color: var(--body-text); letter-spacing: 0.25px; }
  .service__button { margin-top: 17px; height: 35px; border: 1px solid #cfd4d8; border-radius: 3px; background: linear-gradient(#f7f8f9, #e2e6e9); box-shadow: 0 2px 2px rgba(0,0,0,0.12); text-align: center; line-height: 34px; font-family: "Ubuntu", sans-serif; font-weight: 700; font-size: 17px; color: #3a3a3a; }

  .site-footer { position: absolute; left: 0; top: 1053px; width: 1200px; height: 107px; background: var(--footer); color: var(--footer-text); }
  .social { position: absolute; left: 118px; top: 18px; display: flex; align-items: center; }
  .social__label { font-family: "Ubuntu", sans-serif; font-size: 17px; letter-spacing: 1px; color: var(--white); margin-right: 17px; }
  .social__dot { width: 36px; height: 36px; border-radius: 50%; margin-right: 15px; }
  .copyright { position: absolute; left: 119px; top: 72px; font-size: 12.5px; color: var(--footer-text); }
  .footer-brand { position: absolute; left: 920px; top: 30px; display: flex; align-items: center; gap: 10px; }
  .footer-brand__mark { width: 44px; height: 44px; border-radius: 50%; background: #cfcfcf; }
  .footer-brand__name { font-family: "Ubuntu", sans-serif; font-size: 24px; color: #eaeaea; }
</style>
</head>
<body>
  <div class="topbar">
    <div class="topbar__links">Subscribe By <b>RSS</b> or <b>Email</b>
      <svg width="12" height="12" viewBox="0 0 12 12" aria-hidden="true"><circle cx="2" cy="10" r="1.6" fill="#777"/><path d="M1 5a6 6 0 0 1 6 6M1 1a10 10 0 0 1 10 10" stroke="#777" stroke-width="1.6" fill="none"/></svg>
    </div>
  </div>

  <header class="site-header">
    <div class="brand"><div class="brand__mark"></div><span class="brand__name">L. Marvelo</span></div>
    <nav class="main-nav">
      <a class="is-active" href="#">ABOUT</a>
      <a href="#">WORK</a>
      <a href="#">CLIENTS</a>
      <a href="#">SERVICES</a>
      <a href="#">CONTACT</a>
    </nav>
  </header>

  <section class="hero">
    <span class="hero__bubble" style="left:-30px;top:170px;width:100px;height:100px"></span>
    <span class="hero__bubble" style="left:108px;top:350px;width:130px;height:130px"></span>
    <span class="hero__bubble" style="left:1060px;top:5px;width:130px;height:130px"></span>
    <span class="hero__bubble" style="left:1140px;top:30px;width:70px;height:70px"></span>
    <span class="hero__bubble" style="left:780px;top:-40px;width:110px;height:60px"></span>
    <div class="hero__photo" role="img" aria-label="Photo of a young team working at a broadcast mixing desk with headsets"></div>
    <div class="hero__caption">
      <h1 class="hero__title">Audio/Video Production</h1>
      <p class="hero__text">The point of using Lorem Ipsum is that it has a more-or-less normal distribution of letters, as opposed to using 'Content here, content here', making it look like readable English.</p>
      <span class="hero__button">READ MORE</span>
    </div>
    <svg class="hero__arrow" style="left:87px" viewBox="0 0 44 44" aria-label="Previous slide" role="img">
      <circle cx="22" cy="22" r="21" fill="#1b1b1b" stroke="#8a2226" stroke-width="3"/>
      <path d="M25 14l-8 8 8 8" stroke="#fff" stroke-width="4" fill="none" stroke-linecap="round" stroke-linejoin="round"/>
    </svg>
    <svg class="hero__arrow" style="left:1066px" viewBox="0 0 44 44" aria-label="Next slide" role="img">
      <circle cx="22" cy="22" r="21" fill="#1b1b1b" stroke="#8a2226" stroke-width="3"/>
      <path d="M19 14l8 8-8 8" stroke="#fff" stroke-width="4" fill="none" stroke-linecap="round" stroke-linejoin="round"/>
    </svg>
  </section>

  <section class="services">
    <article class="service" style="left:100px">
      <h2 class="service__title">Graphic Design</h2>
      <div class="service__art" role="img" aria-label="Illustration of a light bulb" style="background:linear-gradient(180deg, #f3eaa0 0%, #d9c84a 55%, #a9a9b0 100%)"></div>
      <p class="service__text">Praesent ac massa nec dui faucibus ornare at ac ipsum. Curabitur tempor hendrerit ante, eget ultricies nisl viverra ac. Fusce turpis leo, vestibulum mattis porttitor sed, adipiscing in tellus. Curabitur magna urna, lobortis ut commodo ut, sollicitudin sed sapien. Maecenas vitae mi id libero vulputate egestas vitae fringilla quam.</p>
      <div class="service__button">read more</div>
    </article>
    <article class="service" style="left:440px">
      <h2 class="service__title">Web Development</h2>
      <div class="service__art" role="img" aria-label="Illustration of a globe" style="background:linear-gradient(180deg, #3d8fc8 0%, #2a6a9a 55%, #b9bf3a 100%)"></div>
      <p class="service__text">Praesent ac massa nec dui faucibus ornare at ac ipsum. Curabitur tempor hendrerit ante, eget ultricies nisl viverra ac. Fusce turpis leo, vestibulum mattis porttitor sed, adipiscing in tellus. Curabitur magna urna, lobortis ut commodo ut, sollicitudin sed sapien. Maecenas vitae mi id libero vulputate egestas vitae fringilla quam.</p>
      <div class="service__button">read more</div>
    </article>
    <article class="service" style="left:781px">
      <h2 class="service__title">Apparel Design</h2>
      <div class="service__art" role="img" aria-label="Illustration of a billboard with a paintbrush" style="background:linear-gradient(180deg, #d84a4a 0%, #b52a2a 55%, #8fb4d0 100%)"></div>
      <p class="service__text">Praesent ac massa nec dui faucibus ornare at ac ipsum. Curabitur tempor hendrerit ante, eget ultricies nisl viverra ac. Fusce turpis leo, vestibulum mattis porttitor sed, adipiscing in tellus. Curabitur magna urna, lobortis ut commodo ut, sollicitudin sed sapien. Maecenas vitae mi id libero vulputate egestas vitae fringilla quam.</p>
      <div class="service__button">read more</div>
    </article>
  </section>

  <footer class="site-footer">
    <div class="social">
      <span class="social__label">SOCIAL MEDIA:</span>
      <span class="social__dot" style="background:#3b5a9a" aria-label="Social network one" role="img"></span>
      <span class="social__dot" style="background:#2a9fd8" aria-label="Social network two" role="img"></span>
      <span class="social__dot" style="background:#c8352a" aria-label="Social network three" role="img"></span>
      <span class="social__dot" style="background:#b51d1d" aria-label="Social network four" role="img"></span>
    </div>
    <p class="copyright">Copyright © 2013 - All rights reserved. Terms and Privacy Policy</p>
    <div class="footer-brand"><div class="footer-brand__mark"></div><span class="footer-brand__name">L. Marvelo</span></div>
  </footer>
</body>
</html>
```